I need a design for box for a new product

We are a small business with many awards and loads of customers in the grooming/pet industry. I am attaching a color pattern/theme to go along with the box. The name of the product is MISTORVA MAX: The Complete All-Round Mister Wand. It uses a blue infrared light to help kill 99% of bacteria, along with a canister to put a multitude of liquids/solutions in. It is ideal for sanitizing and protecting grooming salons, kennels, doggy daycare, boarding facilities, vet clinics, animal shelters, barns, and more! Some of the benefits of the Mistorva Max are, but not limited to:
Continuous Spray that reaches over 6 feet in distance, a simple hold of the button for 2 seconds starts the autospray, a much easier alternative than spraying a pump bottle. Comes with a USB-C Charger and charging time only takes 2 hours for a full 50 minutes of run time.

Target Market(s)

Pet Industry Professionals

Industry/Entity Type

Pet Industry

Colors
F0912C
F2A743
F7CA91
FBE8D2
FDF5EE

Requirements
Must have
• A picture of our actual spray gun on the box, worked into the pattern - may need to be photoshopped a bit - do your magic

```html
<!DOCTYPE html>
<html lang="en">
<head>
<meta charset="utf-8">
<title>Mistorva Max – Box Dieline</title>
<link href="https://fonts.googleapis.com/css2?family=Archivo:wght@600;700;800&family=Inter:wght@400;500;700&display=swap" rel="stylesheet">
<style>
  :root {
    --page: #f4e6ea;
    --coral: #f0605a;
    --coral-deep: #e04e4a;
    --navy: #1a2b45;
    --navy-ink: #0f1a33;
    --line: #1b1b1f;
    --white: #ffffff;
  }
  html, body {
    margin: 0;
    width: 1200px;
    height: 1122px;
    overflow: hidden;
    background: var(--page);
  }
  .canvas {
    position: relative;
    width: 1200px;
    height: 1122px;
    display: flex;
    align-items: center;
    justify-content: center;
  }
  .dieline { width: 1170px; height: auto; display: block; }
  .cut { fill: none; stroke: var(--line); stroke-width: 1.6; stroke-linejoin: round; }
  .panel-coral { fill: var(--coral); }
  .panel-navy { fill: var(--navy); }
  .title-pill { fill: var(--navy-ink); }
  .title { font-family: "Archivo", sans-serif; font-weight: 800; fill: var(--white); letter-spacing: 1px; }
  .tagline { font-family: "Inter", sans-serif; font-weight: 400; fill: var(--navy-ink); }
  .brand { font-family: "Archivo", sans-serif; font-weight: 700; fill: var(--navy-ink); letter-spacing: 1px; }
  .side-label { font-family: "Inter", sans-serif; font-weight: 500; fill: #f3b7b2; letter-spacing: .5px; }
  .body-copy { font-family: "Inter", sans-serif; font-size: 9.6px; fill: var(--navy-ink); }
  .body-copy .strong { font-weight: 700; }
  .param-pill { fill: var(--navy-ink); }
  .param-label { font-family: "Inter", sans-serif; font-weight: 700; font-size: 10px; fill: var(--white); }
  .spec { font-family: "Inter", sans-serif; font-size: 9.4px; fill: var(--navy-ink); }
  .rule { stroke: var(--navy-ink); stroke-width: 1.6; }
  .web { font-family: "Archivo", sans-serif; font-weight: 700; font-size: 19px; fill: var(--navy-ink); letter-spacing: .6px; }
  .mark { fill: #f3b7b2; }
</style>
</head>
<body>
<main class="canvas">
  <svg class="dieline" viewBox="240 995 1510 820" xmlns="http://www.w3.org/2000/svg">
    <defs>
      <linearGradient id="splatter-left" x1="0" y1="0" x2="1" y2="0.4">
        <stop offset="0" stop-color="#2a2f45"/>
        <stop offset="0.55" stop-color="#6b3a4a"/>
        <stop offset="1" stop-color="#c9504f"/>
      </linearGradient>
      <linearGradient id="splatter-right" x1="0" y1="0" x2="0.3" y2="1">
        <stop offset="0" stop-color="#e65a55"/>
        <stop offset="1" stop-color="#3a2d44"/>
      </linearGradient>
      <linearGradient id="gun-art" x1="0" y1="0" x2="0" y2="1">
        <stop offset="0" stop-color="#ec6b64"/>
        <stop offset="1" stop-color="#e25a55"/>
      </linearGradient>
    </defs>

    <!-- Printed panels -->
    <g class="print">
      <rect class="panel-coral" x="257" y="1220" width="715" height="456"/>
      <rect x="257" y="1220" width="243" height="456" fill="url(#splatter-left)" role="img" aria-label="Navy paint splatter texture with grooming scissors"/>
      <rect x="890" y="1240" width="82" height="436" fill="url(#splatter-right)" role="img" aria-label="Navy paint splatter texture with grooming scissors"/>
      <rect class="panel-navy" x="972" y="1220" width="176" height="456"/>
      <rect class="panel-coral" x="1148" y="1220" width="544" height="456"/>
    </g>

    <!-- Front panel -->
    <g class="front">
      <rect class="title-pill" x="583" y="1288" width="232" height="31" rx="15.5"/>
      <text class="title" x="699" y="1312" font-size="22" text-anchor="middle">MISTORVA MAX</text>
      <text class="tagline" x="699" y="1345" font-size="16.5" text-anchor="middle">The Complete All-Round Mister Wand</text>
      <rect x="565" y="1385" width="268" height="200" rx="6" fill="url(#gun-art)" role="img" aria-label="Line drawing of the mister wand spray gun"/>
      <text class="brand" x="699" y="1648" font-size="17.5" text-anchor="middle">KINDRED PET SUPPLY</text>
    </g>

    <!-- Side panel -->
    <g class="side">
      <g class="marks" role="img" aria-label="Certification and recycling marks">
        <circle class="mark" cx="995" cy="1619" r="7"/>
        <circle class="mark" cx="1021" cy="1619" r="7"/>
        <circle class="mark" cx="1046" cy="1619" r="7"/>
        <circle class="mark" cx="1071" cy="1619" r="7"/>
        <rect class="mark" x="1091" y="1612" width="11" height="14"/>
        <path class="mark" d="M1112 1627 L1122 1610 L1132 1627 Z"/>
      </g>
      <text class="side-label" x="1061" y="1647" font-size="11" text-anchor="middle">MADE IN CHINA</text>
    </g>

    <!-- Back panel -->
    <g class="back">
      <text class="body-copy">
        <tspan x="1212" y="1277">It uses a blue infrared light to help kill 99% of bacteria, along with a canister to put a</tspan>
        <tspan x="1212" y="1290">multitude of liquids/solutions in</tspan>
        <tspan x="1212" y="1310">It is ideal for sanitizing and protecting grooming salons, kennels, doggy daycare boarding</tspan>
        <tspan x="1212" y="1323">facilities, vet clinics, animal shelters, barns, and more</tspan>
        <tspan x="1212" y="1346" class="strong">Some of the benefits of the Mistorva Max are, but not limited to:</tspan>
        <tspan x="1212" y="1362">Continuous Spray that reaches over 6 feet distance, a simple hold of the button for 2 second</tspan>
        <tspan x="1212" y="1375">starts the autospray, a much easier alternative than spraying a pump bottle. Comes with</tspan>
        <tspan x="1212" y="1388">USB - C Charger and charging time only takes 2 hours for a full 50 minutes of run time.</tspan>
      </text>
      <line class="rule" x1="1207" y1="1426" x2="1640" y2="1426"/>
      <rect class="param-pill" x="1213" y="1437" width="73" height="15" rx="7.5"/>
      <text class="param-label" x="1249.5" y="1448" text-anchor="middle">Parameter</text>
      <text class="spec">
        <tspan x="1213" y="1465">- Material : ABS +PC</tspan>
        <tspan x="1213" y="1478.5">- Motor : Model 528 Custom Motor</tspan>
        <tspan x="1213" y="1492">- Greatest Pressure : 280Kpa - 350Kpa</tspan>
        <tspan x="1213" y="1505.5">- Maximum Flow : 17L - 20L/min</tspan>
        <tspan x="1213" y="1519">- Spray Range : 2.5 - 3m</tspan>
        <tspan x="1213" y="1532.5">- Charging Interface : Type - C</tspan>
        <tspan x="1213" y="1546">- Charging Voltage/Current : 5V - 2A</tspan>
        <tspan x="1213" y="1559.5">- Sound : &lt; 60dB</tspan>
        <tspan x="1213" y="1573">- Operating Temperature : 5ºc -45ºC</tspan>
        <tspan x="1213" y="1599">Made in China</tspan>
      </text>
      <text class="spec">
        <tspan x="1438" y="1465">- Exclusive Dual - Channel Nozzle Design,</tspan>
        <tspan x="1448" y="1478.5">Long Range, No Clogging</tspan>
        <tspan x="1438" y="1492">- Spray Diameter 30 Microns</tspan>
        <tspan x="1438" y="1505.5">- Spray Distance 2.5m</tspan>
        <tspan x="1438" y="1519">- Intelligent Dual Protection Motherboard</tspan>
        <tspan x="1438" y="1532.5">- Soft Start Design + 5C Power Battery</tspan>
        <tspan x="1438" y="1546">- Universal Type - C Charging Port</tspan>
        <tspan x="1446" y="1559.5">528+370 Type Motor Drive</tspan>
        <tspan x="1438" y="1573">- The Maximum Pressure can Reach :</tspan>
        <tspan x="1446" y="1586.5">280Kpa - 350Kpa</tspan>
        <tspan x="1438" y="1600">- Flow Rate : 17L - 20L/Min</tspan>
      </text>
      <text class="web" x="1419" y="1648" text-anchor="middle">WWW.KINDREDPETSUPPLY.COM</text>
    </g>

    <!-- Cut and fold lines -->
    <g class="cut">
      <rect x="257" y="1220" width="1435" height="456"/>
      <line x1="428" y1="1220" x2="428" y2="1676"/>
      <line x1="972" y1="1220" x2="972" y2="1676"/>
      <line x1="1148" y1="1220" x2="1148" y2="1676"/>
      <path d="M260 1220 V1120 H402 L420 1195 L426 1205 V1220"/>
      <path d="M655 1265 V1210 Q655 1178 687 1178 H715 Q745 1178 745 1210 V1265"/>
      <path d="M975 1220 V1205 L982 1195 L1000 1120 H1140 V1220"/>
      <path d="M1148 1220 V1045 H1692 V1220"/>
      <path d="M1150 1045 V1030 Q1150 1008 1180 1008 H1660 Q1690 1008 1690 1030 V1045"/>
      <path d="M1375 1045 V1040 H1465 V1045"/>
      <path d="M1692 1220 L1732 1233 V1662 L1692 1676"/>
      <path d="M257 1676 L343 1755 V1782 Q343 1795 356 1795 H382"/>
      <path d="M400 1795 H426 V1676"/>
      <path d="M430 1676 L510 1760 V1788 Q510 1800 522 1800 H613 Q625 1800 625 1788 V1762 H775 V1788 Q775 1800 787 1800 H878 Q890 1800 890 1788 V1760 L972 1676"/>
      <path d="M975 1676 V1795 H1060 V1755 L1146 1676"/>
      <path d="M1152 1676 V1800 H1228 V1762 H1345 V1788 Q1345 1800 1357 1800 H1483 Q1495 1800 1495 1788 V1762 H1612 V1788 Q1612 1800 1624 1800 H1652"/>
      <path d="M1665 1800 H1688 V1676"/>
    </g>
  </svg>
</main>
</body>
</html>
```